Talvin Foundation Letterhead

We are a newly established non profit registered in Maryland but operates in Africa, south of the sahara. We offer scholarships to deserving young adults from high school through college. Our color theme for our existing logo is purple, we want a design that is stylish, spellbinding yet a letterhead that projects seriousness. More information on www.thetalvinfoundation.example

Target Market(s)

High school and college students in sub saharan African as well as our donors in the US

Industry/Entity Type

Non Profit

Font styles to use
Script

Requirements
Must have
• Logo at the top and if possible watermark the logo in the middle of the letterhead, contact address,
Should not have
• NA

```html
<!DOCTYPE html>
<html lang="en">
<head>
<meta charset="utf-8">
<title>Talvin Foundation Letterhead</title>
<link rel="stylesheet" href="https://fonts.googleapis.com/css2?family=Questrial&display=swap">
<style>
  :root {
    --backdrop: #d2d1d4;
    --paper: #f4f4f4;
    --purple-deep: #774a98;
    --purple-light: #a9a6cf;
    --ink: #6a6a6a;
    --accent: #6b3c95;
    --rule: #b9b9b9;
    --watermark: #e9e9ea;
  }
  * { margin: 0; padding: 0; box-sizing: border-box; }
  html, body { width: 1200px; height: 991px; overflow: hidden; }
  body { background: var(--backdrop); position: relative; }

  .letterhead {
    position: absolute;
    left: 312px; top: 89px;
    width: 577px; height: 813px;
    background: var(--paper);
    box-shadow: 0 1px 3px rgba(0,0,0,.25);
    overflow: hidden;
  }
  .header-band { position: absolute; left: 0; top: 0; width: 577px; height: 80px; }

  .brand {
    position: absolute;
    left: 50px; top: 34px;
    width: 143px;
    text-align: center;
  }
  .brand-circle {
    display: block;
    width: 54px; height: 54px;
    margin: 0 auto 14px;
    border: 3px solid var(--purple-light);
    border-radius: 50%;
    background: var(--paper);
  }
  .brand-name {
    font-family: "Questrial", sans-serif;
    font-weight: 400;
    font-size: 12.4px;
    line-height: 1.1;
    color: var(--purple-deep);
    white-space: nowrap;
  }

  .watermark { position: absolute; left: 86px; top: 255px; width: 400px; height: 400px; }

  .footer {
    position: absolute;
    left: 50px; right: 51px; top: 760px;
    border-top: 0.8px solid var(--rule);
    padding-top: 10px;
    display: flex;
    justify-content: space-between;
    font-family: "Questrial", sans-serif;
    font-size: 7.4px;
    line-height: 1.35;
    color: var(--ink);
  }
  .footer address { font-style: normal; }
  .footer .label, .footer .web-domain { color: var(--accent); font-weight: 700; }
</style>
</head>
<body>
  <main class="letterhead">
    <svg class="header-band" viewBox="0 0 577 80" aria-hidden="true">
      <defs>
        <linearGradient id="bandGradient" x1="0" x2="1" y1="0" y2="0">
          <stop offset="0" stop-color="#774a98"/>
          <stop offset="0.3" stop-color="#8e74b0"/>
          <stop offset="0.57" stop-color="#a9a6cf"/>
          <stop offset="1" stop-color="#8a67a9"/>
        </linearGradient>
      </defs>
      <path d="M0 0 H577 V21 C420 19 220 28 90 56 L0 58 Z" fill="url(#bandGradient)"/>
      <path d="M90 60 C220 32 420 25 577 27" fill="none" stroke="#e2e2e2" stroke-width="3"/>
    </svg>

    <header class="brand">
      <span class="brand-circle"></span>
      <div class="brand-name">Talvin Foundation Inc</div>
    </header>

    <svg class="watermark" viewBox="0 0 400 400" aria-hidden="true">
      <circle cx="200" cy="200" r="188" fill="none" stroke="var(--watermark)" stroke-width="12"/>
    </svg>

    <footer class="footer">
      <address>
        48 Harbour Lane - Suite 12, Annapolis, MD USA, 21401<br>
        <span class="label">Tel:</span> (410) 555-0142 · <span class="label">Email:</span> info@thetalvinfoundation.example
      </address>
      <div class="web">www.<span class="web-domain">thetalvinfoundation</span>.example</div>
    </footer>
  </main>
</body>
</html>
```